Quarry Lane Co. needs Business Cards

For this project, we need business cards (currently have also put a call out for a logo). We are a start-up called Quarry Lane Co. This is our second company (our first one was called Brightwickery). Traditionally we have been providing market research services across different sectors, primarily financial services and the pharmaceutical industry. However, we now want to go beyond market research to offer more (Etc.)... strategic consulting and big data knowledge management. We want our brand to be approachable, creative, fun but professional.

Target Market(s)

The target audience is a business professional - we are B2B (business to business) and do not sell our services to individuals. The brands we work with are major brands across industries, but primarily automotive, financial and pharmaceutical.

Industry/Entity Type

Market Research

Font styles to use
Serif
Sans Serif
Other font styles liked:
• Calibri

Requirements
Must have
• Be clean, simple, modern
Show our address and phone number and email address and website URL
We do not need to have titles showing.

```html
<!DOCTYPE html>
<html lang="en">
<head>
<meta charset="utf-8">
<title>Quarry Lane Co. Business Cards</title>
<link rel="stylesheet" href="https://fonts.googleapis.com/css2?family=Carlito:wght@400;700&display=swap">
<style>
  :root {
    --backdrop: #2b2d2f;
    --card-white: #ffffff;
    --card-black: #000000;
    --accent-grey: #7a7a7a;
    --logo-grey: #6f6f6f;
    --ink-dark: #111111;
    --ink-light: #ffffff;
    --card-radius: 18px;
  }
  * { box-sizing: border-box; margin: 0; padding: 0; }
  html, body {
    width: 1200px;
    height: 720px;
    overflow: hidden;
    background: var(--backdrop);
    font-family: "Carlito", "Calibri", sans-serif;
  }
  .stage {
    position: relative;
    width: 1200px;
    height: 720px;
  }
  .card {
    position: absolute;
    width: 520px;
    height: 300px;
    border-radius: var(--card-radius);
    overflow: hidden;
    box-shadow: 0 14px 30px rgba(0, 0, 0, 0.45);
  }
  /* Back side */
  .card-back {
    left: 50px;
    top: 210px;
    background: var(--card-white);
  }
  .card-back .brand-block {
    position: absolute;
    left: 0;
    right: 0;
    top: 140px;
    text-align: center;
    color: var(--ink-dark);
  }
  .card-back .company-name {
    font-size: 21px;
    font-weight: 700;
    line-height: 1.1;
  }
  .card-back .company-url {
    font-size: 13px;
    font-weight: 700;
    letter-spacing: 0.3px;
  }
  /* Front side */
  .card-front {
    left: 630px;
    top: 210px;
    background: var(--card-black);
  }
  .card-front .shape-layer {
    position: absolute;
    inset: 0;
    width: 520px;
    height: 300px;
  }
  .contact-list {
    position: absolute;
    left: 28px;
    top: 58px;
    list-style: none;
    color: var(--ink-light);
    font-size: 13px;
    letter-spacing: 0.4px;
  }
  .contact-list li {
    display: flex;
    align-items: center;
    height: 20px;
    white-space: nowrap;
  }
  .contact-list li.indent-one { padding-left: 6px; }
  .contact-list li.indent-two { padding-left: 12px; }
  .contact-list li.address-line {
    margin-top: 42px;
    padding-left: 42px;
  }
  .contact-icon {
    width: 15px;
    height: 13px;
    margin-right: 12px;
    flex: none;
  }
  .brand-mark {
    position: absolute;
    left: 338px;
    top: 112px;
    width: 44px;
    height: 34px;
    background: var(--logo-grey);
  }
  .card-front .company-name {
    position: absolute;
    left: 260px;
    width: 200px;
    top: 162px;
    text-align: center;
    font-size: 25px;
    color: var(--ink-dark);
    white-space: nowrap;
  }
</style>
</head>
<body>
<main class="stage">

  <section class="card card-back" aria-label="Business card back">
    <div class="brand-block">
      <p class="company-name">Quarry Lane Co.</p>
      <p class="company-url">www.quarrylaneco.com</p>
    </div>
  </section>

  <section class="card card-front" aria-label="Business card front">
    <svg class="shape-layer" viewBox="0 0 520 300" aria-hidden="true">
      <path d="M215 300 C185 200 220 60 370 0 L520 0 L520 300 Z" fill="#ffffff"/>
      <path d="M232 300 C205 200 245 60 395 0 L520 0 L520 300 Z" fill="#7a7a7a"/>
      <path d="M250 300 C228 200 265 55 420 0 L520 0 L520 300 Z" fill="#ffffff"/>
    </svg>

    <ul class="contact-list">
      <li>
        <svg class="contact-icon" viewBox="0 0 15 13" aria-hidden="true">
          <path d="M1 4 Q7.5 -1 14 4 L12 5.5 L10 4 L5 4 L3 5.5 Z" fill="#fff"/>
          <rect x="3" y="6" width="9" height="6" rx="1" fill="#fff"/>
          <circle cx="7.5" cy="9" r="1.6" fill="#000"/>
        </svg>
        55 5010 2468
      </li>
      <li class="indent-one">
        <svg class="contact-icon" viewBox="0 0 15 13" aria-hidden="true">
          <rect x="0.5" y="1.5" width="14" height="10" fill="#fff"/>
          <path d="M0.5 1.5 L7.5 7.5 L14.5 1.5" fill="none" stroke="#000" stroke-width="1.2"/>
        </svg>
        hello@quarrylaneco.com
      </li>
      <li class="indent-two">
        <svg class="contact-icon" viewBox="0 0 15 13" aria-hidden="true">
          <circle cx="7.5" cy="6.5" r="5.8" fill="none" stroke="#fff" stroke-width="1.2"/>
          <ellipse cx="7.5" cy="6.5" rx="2.6" ry="5.8" fill="none" stroke="#fff" stroke-width="1"/>
          <line x1="1.7" y1="6.5" x2="13.3" y2="6.5" stroke="#fff" stroke-width="1"/>
        </svg>
        www.quarrylaneco.com
      </li>
      <li class="address-line">
        <svg class="contact-icon" viewBox="0 0 15 13" aria-hidden="true">
          <path d="M7.5 0.5 L15 7 L13 7 L13 12.5 L9 12.5 L9 9 L6 9 L6 12.5 L2 12.5 L2 7 L0 7 Z" fill="#fff"/>
        </svg>
        Location
      </li>
    </ul>

    <div class="brand-mark" aria-hidden="true"></div>
    <p class="company-name">Quarry Lane Co.</p>
  </section>

</main>
</body>
</html>
```